Zielgruppe
Wir sind ein Business Center und vermieten Büro- und Konferenzräume. Wir richten uns an Unternehmen unterschiedlichster Branchen: Freelancer ohne eigenes Büro oder auch große Unternehmen, welche keine eigene freien Vakanzen haben, z. B. für Vorstellungsgespräche.
Aufgabenstellung
Flyer Din Lang, quer, gebunden an der kurzen Seite. 8 Seiten, inkl. Vorder- und Rückseite. Bitte kein Wickelfalz oder ähnliches, sondern eine Broschüre, gebunden mit Klammerheftung!!!
Frisches helles Design, ohne Schnörkel. Bilder mit etwas Text, dazu eine Seite über uns. Rückseite Kontaktdaten. Je eine Doppelseite für Konferenzraumvermietung und eine Doppelseite für Büroraum auf Zeit, eine Doppelseite für unsere weitere Leistungen, Telefonservice (Anrufannahme im namen unserer Kunden).
Unsere Räume sind sehr repräsentativ und modern eingerichtet mit hellen Designermöbeln. Das soll auch in der Broschüre klar werden.

```html
<!DOCTYPE html>
<html lang="de">
<head>
<meta charset="utf-8">
<title>Veltrahaus Broschüre</title>
<link href="https://fonts.googleapis.com/css2?family=Open+Sans:wght@400;600&display=swap" rel="stylesheet">
<style>
:root{
  --green:#8db20d;
  --green-dark:#76980a;
  --ink:#3d3f42;
  --grey:#5a5d61;
  --panel:#4b5053;
  --bg:#e8e9ed;
  --paper:#ffffff;
  --photo-warm:#cfc6bb;
  --photo-office:#d9d8d4;
  --badge:#8a2d86;
}
*{box-sizing:border-box;margin:0;padding:0}
html,body{width:1200px;height:3277px;overflow:hidden}
body{background:var(--bg);font-family:"Open Sans",Arial,sans-serif;color:var(--ink);position:relative}
.abs{position:absolute}
.page{position:absolute;background:var(--paper);box-shadow:0 6px 14px rgba(0,0,0,.12)}
.spread{position:absolute;left:22px;width:1161px;height:414px;background:var(--paper);box-shadow:0 6px 14px rgba(0,0,0,.12)}
.spread::after{content:"";position:absolute;left:578px;top:0;width:1px;height:100%;background:rgba(0,0,0,.08)}
.photo{position:absolute}
.band{position:absolute;background:var(--green);color:#fff}
.bar-title{position:absolute;background:var(--green);color:#fff;font-size:15px;line-height:25px;padding-left:32px;white-space:nowrap}
.body-text{font-size:8px;line-height:1.38;color:#fff}
.body-text p+p{margin-top:9px}
.features{list-style:none;font-size:8px;line-height:1.45;color:#fff;margin-top:16px}
.features li::before{content:"➔";margin-right:6px}

/* cover */
.cover{position:absolute;width:627px;height:448px;background:var(--paper);overflow:hidden}
.brand{position:absolute;display:flex;align-items:center;gap:7px;font-size:20px;font-weight:600;color:var(--grey);letter-spacing:1px}
.brand-square{width:16px;height:16px;border:2px solid var(--green)}
.cover .brand{left:46px;top:52px}
.cover-year{position:absolute;right:37px;top:38px;text-align:right;font-size:8.5px;line-height:1.2;color:var(--ink)}
.cover-year strong{display:block;font-size:22px;font-weight:600;color:var(--green);line-height:1.05}
.cover-photo{left:0;top:126px;width:318px;height:193px;background:linear-gradient(160deg,#e2dcd2,#a89e92);clip-path:polygon(0 0,100% 0,72% 100%,0 100%)}
.cover-band{left:191px;top:168px;width:436px;height:109px;clip-path:polygon(10% 0,100% 0,100% 100%,0 100%)}
.cover-band h1{position:absolute;left:98px;top:32px;font-size:26px;font-weight:400;line-height:.95;letter-spacing:1px}
.cover-lead{position:absolute;left:385px;top:295px;width:205px;font-size:7px;line-height:1.3;color:var(--grey);text-align:justify}
.cover-url{position:absolute;left:0;width:627px;top:381px;text-align:center;font-size:11px;font-weight:600;color:var(--ink)}

.quote{position:absolute;font-size:6.5px;line-height:1.35;color:#e6e6e6;text-align:center}
.quote cite{display:block;margin-top:8px;font-style:normal;font-weight:600;color:#fff;font-size:7.5px}
.quote cite small{font-weight:400;font-size:5.5px}
.avatar{position:absolute;width:40px;height:40px;border-radius:50%;background:#9ea3a6;border:2px solid #fff}
.col-text{position:absolute;font-size:8.5px;line-height:1.3;color:var(--grey)}
.contact{position:absolute;font-size:7px;line-height:1.35;color:#e5efc7}
</style>
</head>
<body>

<!-- Titelseite -->
<section class="cover" style="left:271px;top:74px;box-shadow:0 6px 14px rgba(0,0,0,.12)">
  <div class="brand"><span class="brand-square"></span>VELTRAHAUS</div>
  <div class="cover-year"><strong>2018</strong>DIE MODERNE<br>ART DES MIETENS</div>
  <div class="photo cover-photo" role="img" aria-label="Foto: moderne Bürohochhäuser mit Glasfassade"></div>
  <div class="band cover-band"><h1>NEUE MASSSTÄBE<br>SETZEN</h1></div>
  <p class="cover-lead">Unser modernes Business Center bietet mehr als ein reines Callcenter. Anrufannahme, hochwertigste Mietbüros und ein stylischer Konferenzraum</p>
  <p class="cover-url">www.buero-veltrahaus.de</p>
</section>

<!-- Doppelseite: Willkommen -->
<section class="spread" style="top:687px">
  <h2 class="abs" style="left:54px;top:53px;font-size:24px;font-weight:400;letter-spacing:2px;color:var(--ink)">WILLKOMMEN</h2>
  <div class="photo" style="left:658px;top:45px;width:464px;height:308px;background:linear-gradient(135deg,#eeeeea,#c9c6c0 60%,#9a6a4a)" role="img" aria-label="Foto: heller Konferenzraum mit weißem Tisch, orangefarbenen Stühlen und Bildschirm"></div>
  <div class="band" style="left:251px;top:55px;width:524px;height:25px">
    <span class="abs" style="left:13px;top:2px;font-size:15px">Über uns:</span>
    <span class="abs" style="left:347px;top:7px;font-size:7.5px;color:#eef5d6">Büro auf Zeit - die moderne Art des Mietens</span>
  </div>
  <div class="band" style="left:30px;top:103px;width:815px;height:224px">
    <h3 class="abs" style="left:74px;top:20px;font-size:17px;font-weight:400">Viel mehr als ein Callcenter</h3>
    <div class="abs body-text" style="left:74px;top:56px;width:360px;text-align:justify">
      <p>Im Gründungsjahr 2003 wurde die Idee zu einem Schreibbüro geboren: Briefe verfassen, Mailings versenden, Daten erfassen - das war der Grundgedanke.</p>
      <p>Nach den ersten Jahren entwickelte sich das Unternehmen in eine neue Richtung und der Bereich Telefonservice wurde etabliert.</p>
      <p>Seit mehr als 15 Jahren leisten wir unseren Beitrag für einen optimalen Kundenservice am Telefon. Freundliche Mitarbeiterinnen und Mitarbeiter geben täglich ihr Bestes für viele namhafte Kunden aus ganz Europa. Hierbei legen wir größten Wert auf gut ausgebildete Mitarbeiter, sowie hochwertigste Technik. Daher hat sich VELTRAHAUS 2012, nach einer Testphase, gegen VOIP (Internettelefonie) entschieden. Seit 2012 telefonieren wir wieder mit klassischer ISDN-Technologie vom Netzbetreiber; VOIP kommt für uns auf Grund der mangelnden Qualität weiterhin nicht in Frage!</p>
    </div>
    <div class="abs body-text" style="left:580px;top:21px;width:205px">
      <p>Unsere Räume sind sehr repräsentativ und modern eingerichtet mit hellen Designermöbeln. Der Mietvertrag läuft auf unbestimmte Zeit und ist mit einer Kündigungsfrist von 3 Monaten kündbar. Sie erhalten einen Haustürschlüssel, sowie einen Schlüssel für Ihr privates Büro. Der Zugang ist somit 24/7 möglich.</p>
      <p>Auf Wunsch können wir Ihnen eine Düsseldorfer Rufnummer zu Verfügung stellen und unsere Agenten nehmen Ihre Anrufe entgegen. Dies ist immer dann sinnvoll, wenn Sie selbst nicht im Büro sind.</p>
      <p>Selbstverständlich halten wir Getränke für unsere Mieter bereit, welche Sie am Empfang erwerben können. Ihr Büro wird von unserer Reinigungsfachkraft zweimal pro Woche gereinigt.</p>
    </div>
  </div>
  <div class="band" style="left:0;top:349px;width:253px;height:19px;font-size:7.5px;line-height:19px;padding-left:102px;white-space:nowrap">VELTRAHAUS - alles aus einer Hand</div>
</section>

<!-- Doppelseite: Büroanmietung -->
<section class="spread" style="top:1401px">
  <div class="photo" style="left:15px;top:45px;width:567px;height:314px;background:linear-gradient(120deg,#f2f2f0,#d6d6d3 55%,#6b6b6b)" role="img" aria-label="Foto: heller Schreibtisch mit Laptop, Bürostuhl und Designerleuchte"></div>
  <div class="bar-title" style="left:6px;top:56px;width:251px">Büroanmietung in Düsseldorf</div>
  <div class="band" style="left:6px;top:105px;width:300px;height:224px;padding:22px 10px 0 32px">
    <p class="body-text">Nach Vertragsunterzeichnung können Sie sofort einziehen: kein Umbau, keine Renovierung und wenn Sie wünschen, können Sie das Mietverhältnis kurzfristig wieder kündigen. Soviel Flexibilität erhalten Sie nur bei uns!</p>
    <ul class="features">
      <li>Zugang 24/7</li>
      <li>persönlicher Empfang</li>
      <li>ab 15qm</li>
      <li>eigenes Firmenschild</li>
      <li>wöchentliche Reinigung inklusive</li>
      <li>kostenfreier Hochgeschwindigkeits-Internetzugang</li>
      <li>große Schreibtische</li>
      <li>auf Wunsch inkl. Anrufannahme durch unser geschultes Personal</li>
      <li>optionale Anmietung eines Konferenzraumes mit bis zu 10 Plätzen</li>
      <li>Mitbenutzung der sanitären Einrichtungen und der Küche</li>
    </ul>
  </div>
  <svg class="abs" style="left:624px;top:33px" width="520" height="340" viewBox="0 0 520 340" aria-hidden="true">
    <path d="M420 0H490V95H478V12H420Z" fill="var(--green)"/>
    <path d="M0 238H12V318H100V330H0Z" fill="var(--green)"/>
  </svg>
  <div class="photo" style="left:640px;top:45px;width:240px;height:104px;background:linear-gradient(135deg,#eceae6,#bdb7ae)" role="img" aria-label="Foto: Einzelbüro mit Schreibtisch am Fenster"></div>
  <div class="photo" style="left:880px;top:45px;width:226px;height:314px;background:linear-gradient(160deg,#f1f0ed,#d8d2c8 60%,#c49a68)" role="img" aria-label="Foto: Empfangsbereich mit Holztheke und Blick aus dem Fenster"></div>
  <div class="photo" style="left:640px;top:149px;width:240px;height:106px;background:linear-gradient(135deg,#e6e0d6,#b88d5d)" role="img" aria-label="Foto: Flur mit Holzschränken und Pflanze"></div>
  <div class="photo" style="left:711px;top:255px;width:260px;height:104px;background:linear-gradient(135deg,#dcdcda,#55585c)" role="img" aria-label="Foto: Sitzecke mit Stuhl, Beistelltisch und Kaffeekanne"></div>
  <div class="band" style="left:913px;top:361px;width:249px;height:24px;font-size:10px;line-height:24px;text-align:center">Büro Derendorf mit Blick auf den Rheinturm</div>
</section>

<!-- Doppelseite: Konferenzraum und Kundenstimmen -->
<section class="spread" style="top:2092px">
  <div class="photo" style="left:100px;top:42px;width:479px;height:319px;background:linear-gradient(120deg,#efeeeb,#d3d0cb 55%,#8b8f92)" role="img" aria-label="Foto: Konferenzraum mit langem Tisch, grauen Stühlen und Flipchart"></div>
  <div class="bar-title" style="left:0;top:55px;width:292px">Konferenzraum anmieten</div>
  <div class="band" style="left:0;top:105px;width:295px;height:226px;padding:9px 10px 0 44px">
    <p class="body-text">Nutzen Sie unsere modernen Konferenz- und Tagungsräume für Meetings, Präsentationen, Gespräche, oder Schulungen. Unsere hellen, stylischen Räume werden auch Sie faszinieren. Präsentieren Sie sich vor Ihren Geschäftspartnern an einem tollen Ort. Unser Team erfüllt all Ihre Wünsche - vom leckeren Cappuccino bishin zu raffinierten Canapes.</p>
    <ul class="features" style="margin-top:12px;line-height:1.4">
      <li>bis zu 10 Teilnehmer</li>
      <li>bekannte Location im Stadthaus am Park</li>
      <li>persönlicher Empfang &amp; Betreuung</li>
      <li>55 Zoll 4k Fernseher</li>
      <li>Streaming-Box</li>
      <li>Bildschirm-Streaming</li>
      <li>Konferenztelefon</li>
      <li>großes Whiteboard</li>
      <li>Flipchart</li>
      <li>Tiefgarage</li>
      <li>auch auf Raumportal buchbar</li>
    </ul>
  </div>
  <div class="band" style="left:291px;top:370px;width:422px;height:19px"></div>

  <svg class="abs" style="left:587px;top:33px" width="570" height="210" viewBox="0 0 570 210" aria-hidden="true">
    <path d="M495 0H545V45H533V12H495Z" fill="var(--green)"/>
    <rect x="0" y="190" width="55" height="12" fill="var(--green)"/>
  </svg>
  <div class="abs" style="left:597px;top:41px;width:548px;height:188px;background:var(--panel)"></div>
  <div class="bar-title" style="left:828px;top:50px;width:251px;padding-left:20px">Das sagen unsere Kunden</div>
  <div class="avatar" style="left:749px;top:97px" role="img" aria-label="Porträtfoto Kunde"></div>
  <div class="avatar" style="left:990px;top:97px" role="img" aria-label="Porträtfoto Kunde"></div>
  <p class="quote" style="left:656px;top:155px;width:228px">❝ Ich nutze den Telefonservice von VELTRAHAUS seit ca. einem halben Jahr und bin sehr zufrieden. Wichtig sind mir insbesondere, dass Anrufe zuverlässig und rasch entgegen genommen werden können, sowie die Freundlichkeit der Mitarbeiter von VELTRAHAUS. In beiden Punkten wurden meine Erwartungen an einen Telefonservice voll erfüllt! ❞
    <cite>- Marek Lindholm <small>www.praxis-lindholm.de</small></cite></p>
  <p class="quote" style="left:895px;top:155px;width:226px">❝ Seit mehr als 2 Jahren nutze ich den Telefonservice von VELTRAHAUS. Mich überzeugt nach wie vor die absolut professionelle Leistung, verbunden mit dem besten Preis/Leistungsverhältnis. Ich freue mich, dass ich VELTRAHAUS gefunden habe! ❞
    <cite>- Anselm Krewitt, Praxis Dr. Holm <small>www.praxis-holm.de</small></cite></p>
  <p class="col-text" style="left:620px;top:282px;width:252px">Unsere freundlichen Damen begrüßen Ihre Besucher und führen Sie in den Besprechungsraum. Auf Wunsch stellen wir auch einen Beamer mit Leinwand zur Verfügung. Wir empfehlen aber immer unseren großen Bildschirm mit 4k für brilliante Präsentationen zu nutzen - die Qualität wird auch Sie überzeugen.</p>
  <p class="col-text" style="left:889px;top:282px;width:227px">Sollte Ihr Meeting einmal länger dauern, können Sie gerne mit uns ein indivduelles Catering planen: vom klassischen Mettbrötchen bis hin zu raffinierter italischer Antipasta bleiben keine Wünsche offen.</p>
  <div class="abs" style="left:1058px;top:322px;width:54px;height:54px;border-radius:50%;background:var(--badge)" role="img" aria-label="Auszeichnungs-Siegel"></div>
</section>

<!-- Rückseite und Titel -->
<section class="spread" style="top:2822px;height:420px">
  <div class="abs" style="left:18px;top:47px;width:547px;height:310px;background:linear-gradient(90deg,var(--green-dark),var(--green))"></div>
  <div class="abs" style="left:18px;top:83px;width:214px;height:34px;background:var(--paper)"></div>
  <div class="brand" style="left:244px;top:150px;color:#fff"><span class="brand-square" style="border-color:#fff"></span>VELTRAHAUS</div>
  <p class="contact" style="left:155px;top:238px">VELTRAHAUS<br>Lindenweg 42<br>40210 Düsseldorf<br><br>BÜROZEITEN<br>Mo.-Fr. 08:00 - 20:00</p>
  <p class="contact" style="left:284px;top:238px">TELEFON<br>0800 555 0199<br><br><br>EMAIL<br>info@veltrahaus.de</p>

  <div class="cover" style="left:575px;top:0;transform:scale(.935);transform-origin:0 0">
    <div class="brand"><span class="brand-square"></span>VELTRAHAUS</div>
    <div class="cover-year"><strong>2018</strong>DIE MODERNE<br>ART DES MIETENS</div>
    <div class="photo cover-photo" role="img" aria-label="Foto: moderne Bürohochhäuser mit Glasfassade"></div>
    <div class="band cover-band"><h1>NEUE MASSSTÄBE<br>SETZEN</h1></div>
    <p class="cover-lead">Unser modernes Business Center bietet mehr als ein reines Callcenter. Anrufannahme, hochwertigste Mietbüros und ein stylischer Konferenzraum</p>
    <p class="cover-url">www.buero-veltrahaus.de</p>
  </div>
</section>

</body>
</html>
```